Website for my photography business

I need a website for my photography business, Jonah Pelling Photography. I need a website that has a landing page with a cover photo of each kind of photography I do. For example, Nature, Weddings, Portraits and Architecture. I want it so that when someone comes onto my website they have to choose which kind of photography page they want to visit. So if they click on the wedding photo it will open to a page with my wedding portfolio images and a contact me button. If they choose nature photography I want them to be redirected to an e-commerce section where they can purchase prints. Architecture and Portraits should open up to their respective portfolios with about me and contact info. I like this kind of format because I want people who come to my website for a specific type of photography to be able to be directed there easily without having to look at a mix of other kinds of photography. I will provide a few files to use as placeholders. I have already purchased the jonahpellingphotography.example domain name. A Wix website would be great because I am most familiar with it but I am open to anything.

Industry/Entity Type

Photographer

Number of Pages Required

5+ page

Requirements
Must have
• Landing Page and e-commerce

```html
<!DOCTYPE html>
<html lang="en">
<head>
<meta charset="UTF-8">
<title>Portrait Photo Gallery – Jonah Pelling Photography</title>
<link rel="stylesheet" href="https://fonts.googleapis.com/css2?family=Parisienne&family=Roboto:wght@400&display=swap">
<style>
  :root {
    --page-bg: #ffffff;
    --ink: #000000;
    --brand-ink: #4a4a78;
    --portrait-light: #d2d2d2;
    --portrait-dark: #9a9a9a;
    --photo-dark: #2e2e2e;
    --photo-mid: #7d7d7d;
    --photo-light: #cfcfcf;
    --footer-bg: #000000;
    --footer-ink: #ffffff;
  }
  * { margin: 0; padding: 0; box-sizing: border-box; }
  html, body { width: 1200px; height: 994px; overflow: hidden; background: var(--page-bg); }
  .page { position: relative; width: 1200px; height: 994px; font-family: "Roboto", sans-serif; color: var(--ink); }

  .brand {
    position: absolute; top: 20px; left: 0; width: 1200px; text-align: center;
    font-family: "Parisienne", cursive; font-size: 20px; line-height: 1; color: var(--brand-ink);
  }

  .section-title {
    position: absolute; left: 58px;
    font-family: "Parisienne", cursive; font-weight: 400; font-size: 34px; line-height: 1;
  }
  .gallery-title { top: 80px; }
  .about-title { top: 443px; }

  .gallery { position: absolute; top: 150px; left: 0; width: 1200px; height: 258px; display: flex; overflow: hidden; }
  .gallery-photo {
    flex: 0 0 262.5px; height: 258px;
    background:
      radial-gradient(ellipse 70% 55% at 62% 30%, var(--photo-light) 0%, transparent 70%),
      linear-gradient(160deg, var(--photo-mid) 0%, var(--photo-dark) 45%, var(--photo-mid) 75%, var(--photo-light) 100%);
  }
  .gallery-next {
    position: absolute; top: 0; right: 0; width: 38px; height: 258px;
    background: rgba(255,255,255,0.35);
    display: flex; align-items: center; justify-content: center;
  }

  .about-photo {
    position: absolute; top: 499px; left: 58px; width: 258px; height: 334px;
    background: linear-gradient(180deg, var(--portrait-light) 0%, var(--portrait-dark) 100%);
  }

  .about-text {
    position: absolute; top: 500px; left: 430px; width: 660px;
    font-size: 14.5px; line-height: 17.5px;
  }

  .contact-button {
    position: absolute; top: 797px; left: 431px; width: 131px; height: 36px;
    border: 1px solid var(--ink); background: var(--page-bg); color: var(--ink); text-decoration: none;
    font-family: "Parisienne", cursive; font-size: 19px;
    display: flex; align-items: center; justify-content: center;
  }

  .site-footer {
    position: absolute; left: 0; top: 931px; width: 1200px; height: 63px;
    background: var(--footer-bg); color: var(--footer-ink); font-size: 10px; line-height: 12px; text-align: center;
  }
  .footer-name { position: absolute; top: 14px; width: 100%; }
  .footer-contact { position: absolute; top: 33px; width: 100%; }
  .footer-contact span + span { margin-left: 30px; }
</style>
</head>
<body>
<div class="page">
  <header class="brand">Jonah Pelling Photography</header>

  <h1 class="section-title gallery-title">Portrait Photo Gallery</h1>

  <section class="gallery">
    <div class="gallery-photo" role="img" aria-label="Black and white figure portrait photograph"></div>
    <div class="gallery-photo" role="img" aria-label="Black and white figure portrait photograph"></div>
    <div class="gallery-photo" role="img" aria-label="Black and white figure portrait photograph"></div>
    <div class="gallery-photo" role="img" aria-label="Black and white figure portrait photograph"></div>
    <div class="gallery-photo" role="img" aria-label="Black and white figure portrait photograph"></div>
    <div class="gallery-next">
      <svg width="16" height="26" viewBox="0 0 16 26" aria-label="Next">
        <polyline points="3,3 13,13 3,23" fill="none" stroke="#000" stroke-width="2.5"/>
      </svg>
    </div>
  </section>

  <h2 class="section-title about-title">About Me</h2>

  <div class="about-photo" role="img" aria-label="Portrait photograph of Jonah Pelling"></div>

  <p class="about-text">Hi, I'm Jonah. I have been photographing people for more than twelve years, and portraits remain the work closest to my heart. My approach is calm and unhurried: we talk, we take our time, and the camera slowly disappears until what is left is simply you. I work mostly in natural light and in black and white, because I believe tone, shape and texture can say more about a person than colour ever could. Every session begins with a conversation about who you are and what you would like your portraits to express, whether that is strength, tenderness, confidence or quiet reflection. Sessions take place in my studio, in your home or at a location that means something to you, and each one is planned around your comfort. I shoot individuals, couples and families, as well as creative and fine art figure studies for clients who want something bolder. After the session I carefully edit every image by hand, keeping skin and light honest rather than perfect, and deliver a private online gallery within two weeks. Archival prints and hand-bound albums are available for those who want to hold their photographs and pass them on. If you are curious about booking a portrait session, or simply have a question about how it all works, I would love to hear from you.</p>

  <a class="contact-button" href="#contact">Contact Me</a>

  <footer class="site-footer" id="contact">
    <div class="footer-name">Jonah Pelling Photography</div>
    <div class="footer-contact"><span>Phone: +1 555-014-2278</span><span>Email: hello@jonahpellingphotography.example</span></div>
  </footer>
</div>
</body>
</html>
```